BLQ Business Card

We need a business card that reflect our business, we have put anther business card as an example of what we like but please feel free to do your own thing.

Here are the items to be placed on card

Wade Pelham
Amber Harbor Supply
Mobile: 917-555-4820
Office: 516-555-7164
Fax: 866-555-3291
Email: info@amberharborsupply-example.com
Website: amberharborsupply-example.com

I have added raw files to upload

Wade Pelham
Amber Harbor Supply
Mobile: 917-555-4820
Office: 516-555-7164
Fax: 866-555-3291 

Target Market(s)

Natural product manufactures, and retailers and distributors

Industry/Entity Type

Business

Requirements
Must have
• 1. Logo
2. The colors of the company

```html
<!DOCTYPE html>
<html lang="en">
<head>
<meta charset="utf-8">
<title>Amber Harbor Supply – Business Card</title>
<link rel="stylesheet" href="https://fonts.googleapis.com/css2?family=Open+Sans:wght@400;800&display=swap">
<style>
  :root {
    --brand-green: #6db545;
    --ink-black: #000000;
    --paper-white: #ffffff;
  }
  html, body {
    margin: 0;
    padding: 0;
    width: 1200px;
    height: 1200px;
    overflow: hidden;
    background: var(--paper-white);
  }
  .canvas {
    position: relative;
    width: 1200px;
    height: 1200px;
    font-family: "Open Sans", sans-serif;
  }
  .card {
    position: absolute;
    display: block;
  }
  .card--front { left: 267px; top: 138px; width: 540px; height: 313px; }
  .card--back  { left: 274px; top: 546px; width: 542px; height: 312px; }
  .fill-green { fill: var(--brand-green); }
  .fill-black { fill: var(--ink-black); }
  .fill-white { fill: var(--paper-white); }
  .card-border { fill: none; stroke: var(--ink-black); stroke-width: 1; }
  .brand-name {
    font-family: "Open Sans", sans-serif;
    font-weight: 800;
    font-size: 44px;
    fill: var(--brand-green);
    letter-spacing: -1px;
  }
  .contact-line {
    font-family: "Open Sans", sans-serif;
    font-weight: 400;
    font-size: 19px;
  }
  .contact-line--dark { fill: var(--ink-black); font-size: 18px; }
  .contact-line--green { fill: var(--brand-green); }
  .person-name {
    font-family: "Open Sans", sans-serif;
    font-size: 25px;
    fill: var(--brand-green);
  }
</style>
</head>
<body>
<main class="canvas">

  <svg class="card card--front" viewBox="0 0 630 365" aria-label="Business card front">
    <rect class="fill-white" x="0" y="0" width="630" height="365"/>
    <path class="fill-black" d="M0,0 L630,0 C520,20 440,60 395,90 L245,90 C200,60 120,25 0,0 Z"/>
    <path class="fill-green" d="M0,365 C100,340 190,300 240,250 L390,250 C440,300 530,350 630,365 Z"/>
    <rect class="fill-white" x="15" y="110" width="600" height="130"/>
    <text class="brand-name" x="315" y="192" text-anchor="middle">Amber Harbor Supply</text>
    <rect class="card-border" x="0.5" y="0.5" width="629" height="364"/>
  </svg>

  <svg class="card card--back" viewBox="0 0 632 365" aria-label="Business card back">
    <rect class="fill-green" x="0" y="0" width="632" height="365"/>
    <path class="fill-black" d="M0,0 C200,40 318,120 318,182 C318,244 200,324 0,365 Z"/>
    <path class="fill-black" d="M632,0 C432,40 318,120 318,182 C318,244 432,324 632,365 Z"/>
    <text class="contact-line contact-line--dark" x="316" y="28" text-anchor="middle">email:info@amberharborsupply-example.com</text>
    <text class="person-name" x="16" y="167">Wade Pelham</text>
    <text class="contact-line contact-line--green" x="17" y="203">Amber Harbor Supply</text>
    <text class="contact-line contact-line--green" x="392" y="169">Mobile: 917-555-4820</text>
    <text class="contact-line contact-line--green" x="392" y="197">Office: 516-555-7164</text>
    <text class="contact-line contact-line--green" x="396" y="224">Fax: 866-555-3291</text>
    <text class="contact-line contact-line--dark" x="314" y="349" text-anchor="middle">website:amberharborsupply-example.com</text>
  </svg>

</main>
</body>
</html>
```